Management consultant needs business cards

We need a design for a personal/professional business card for a management consultant. Work is typically focused on the b2b space, helping companies improve their operations. The final design should communicate efficiency and helping companies and people achieve their full potential.

Company name is "Copperfen Consultants"

Brand promise is "Spotting Strengths - Sharpening Operations"

We come from major consulting firms (Haldorne, Vesk, TQP) but would like to project a slightly more modern feel than those players.

Target Market(s)

Targeting B2B markets such as banks or companies.

Industry/Entity Type

Business

Requirements
Must have
• The card must communicate the following information:

Nolan J Brackett
Managing Director
Copperfen Consultants
Phone: 416-555-0172
nolan.brackett@copperfenconsultants.example
www.copperfenconsultants.example

214 Pellworth Ave
Toronto, ON M5X 9Z7

Back side should have
"Spotting Strengths - Sharpening Operations"

```html
<!DOCTYPE html>
<html lang="en">
<head>
<meta charset="utf-8">
<title>Copperfen Consultants – Business Card</title>
<link rel="stylesheet" href="https://fonts.googleapis.com/css2?family=Source+Sans+3:wght@400&family=Arimo:wght@400&display=swap">
<style>
  :root {
    --page: #ffffff;
    --card: #373435;
    --frame: #1e9ad6;
    --accent: #f58a2f;
    --ink: #ffffff;
    --font-front: "Source Sans 3", "Myriad Pro", sans-serif;
    --font-back: "Arimo", Arial, sans-serif;
  }
  html, body {
    margin: 0;
    padding: 0;
    width: 1200px;
    height: 324px;
    overflow: hidden;
    background: var(--page);
  }
  .sheet {
    position: relative;
    width: 1200px;
    height: 324px;
  }
  .card {
    position: absolute;
    top: 0;
    width: 571px;
    height: 324px;
    background: var(--card);
    color: var(--ink);
  }
  .card--front { left: 0; font-family: var(--font-front); }
  .card--back { left: 629px; }
  .card__frame {
    position: absolute;
    left: 16px;
    top: 16px;
    right: 16px;
    bottom: 16px;
    border: 1.5px solid var(--frame);
  }
  .line {
    position: absolute;
    margin: 0;
    line-height: 1;
    white-space: nowrap;
  }

  /* Front */
  .card--front .line { left: 155px; }
  .holder-name { top: 32px; font-size: 20px; color: var(--accent); }
  .company-name { top: 60px; font-size: 21px; }
  .contact { font-size: 17px; }
  .contact--phone { top: 112px; }
  .contact--email { top: 141px; }
  .contact--street { top: 170px; }
  .contact--city { top: 194px; }
  .website { top: 279px; font-size: 21px; }

  /* Back */
  .card--back .line { transform: translateX(-50%); }
  .back-name { left: 267px; top: 97px; font-size: 29px; font-family: var(--font-front); }
  .back-title { left: 276px; top: 158px; font-size: 16px; font-family: var(--font-back); }
  .tagline { left: 286px; top: 226px; font-size: 17px; font-family: var(--font-back); }
  .divider {
    position: absolute;
    left: 0;
    top: 150px;
    width: 571px;
    height: 40px;
  }
</style>
</head>
<body>
<main class="sheet">
  <section class="card card--front" aria-label="Card front">
    <div class="card__frame"></div>
    <p class="line holder-name">Nolan J Brackett</p>
    <p class="line company-name">Copperfen Consultants</p>
    <p class="line contact contact--phone">Phone: 416-555-0172</p>
    <p class="line contact contact--email">E-mail: nolan.brackett@copperfenconsultants.example</p>
    <p class="line contact contact--street">214 Pellworth Ave</p>
    <p class="line contact contact--city">Toronto, ON M5X 9Z7</p>
    <p class="line website">www.copperfenconsultants.example</p>
  </section>

  <section class="card card--back" aria-label="Card back">
    <div class="card__frame"></div>
    <p class="line back-name">Nolan J Brackett</p>
    <svg class="divider" viewBox="0 0 571 40" aria-hidden="true">
      <rect x="0" y="16" width="164" height="8" fill="var(--accent)"/>
      <rect x="406" y="16" width="165" height="8" fill="var(--accent)"/>
      <polygon transform="translate(170 20)" fill="var(--ink)"
        points="0,-9 2.12,-2.91 8.56,-2.78 3.42,1.11 5.29,7.28 0,3.6 -5.29,7.28 -3.42,1.11 -8.56,-2.78 -2.12,-2.91"/>
      <polygon transform="translate(399 20)" fill="var(--ink)"
        points="0,-9 2.12,-2.91 8.56,-2.78 3.42,1.11 5.29,7.28 0,3.6 -5.29,7.28 -3.42,1.11 -8.56,-2.78 -2.12,-2.91"/>
    </svg>
    <p class="line back-title">Managing Director</p>
    <p class="line tagline">Spotting Strengths - Sharpening Operations</p>
  </section>
</main>
</body>
</html>
```